Business Card Design Project - KLB

I am looking for a more sophisticated card design for my company,
"The Lumen Collective"

We are a consultancy focused on strategy and change in Associations and professional organisations.

I am a lawyer and psychologist with a PhD and so am looking for something that communicates seriousness and credibility but also quirky creative solutions for strategic problems, which is my field of speciality.

I am looking for something that is quietly spoken, rather than loud colours ('credible' and 'creative' are the two adjectives that I think of as competing here).

I particularly like an embossed card style - heavy white card with plain white or white and black or white and grey text.

The key logo image for the company is a question mark and I am open to suggestions and ideas on design.

I have attached a file that includes a couple of styles that have caught my eye and my thoughts on them. Hopefully they communicate what I'm looking for.
Updates

Thank you for all the great suggestions and designs.

I really appreciated the effort and creative energy you put into your designs. I have now closed the project after selecting a design and advising the successful designer of the card that I am happy with.

Regards

Target Market(s)

Organisations (CEO's and Boards), Governments, Legal professionals, Membership Associations and aspiring professionals.

Industry/Entity Type

Lawyer

Requirements
Must have
• The key logo element is a question mark (?) and this needs to be incorporated.

Embossed style - cut outs or other design ideas interest me too.

The attached file has a number of sample ideas and comments on each one that I like.
Should not have
• I like crisp, modern fonts (Myriads etc...) and do not like embellished fonts or Times etc...

Files

```html
<!DOCTYPE html>
<html lang="en">
<head>
<meta charset="utf-8">
<title>The Lumen Collective — Business Card</title>
<link rel="stylesheet" href="https://fonts.googleapis.com/css2?family=Arimo:wght@400;700&display=swap">
<style>
  :root {
    --card-white: #ffffff;
    --panel-dark: #1d1d1d;
    --ink-logo: #2b2b2b;
    --ink-muted: #3e3e3e;
  }
  html, body {
    margin: 0;
    padding: 0;
    width: 1200px;
    height: 568px;
    overflow: hidden;
    background: var(--card-white);
  }
  .card {
    position: relative;
    width: 1200px;
    height: 568px;
    display: flex;
    font-family: "Arimo", Arial, sans-serif;
  }
  .brand-panel {
    width: 413px;
    height: 100%;
    background: var(--card-white);
    display: flex;
    flex-direction: column;
    align-items: center;
    justify-content: center;
    gap: 22px;
  }
  .brand-mark {
    width: 64px;
    height: 64px;
    border-radius: 50%;
    background: var(--ink-logo);
  }
  .brand-name {
    margin: 0;
    color: var(--ink-logo);
    font-weight: 700;
    font-size: 38px;
    line-height: 1.15;
    text-align: center;
    letter-spacing: 0.5px;
  }
  .details-panel {
    flex: 1;
    height: 100%;
    background: var(--panel-dark);
    position: relative;
    color: var(--ink-muted);
    font-weight: 700;
    font-size: 24px;
  }
  .detail {
    position: absolute;
    left: 38px;
    margin: 0;
    white-space: nowrap;
    line-height: 1;
  }
  .person-name { top: 74px; }
  .person-role { top: 104px; }
  .company     { top: 199px; }
  .mobile      { top: 264px; }
  .phone       { top: 327px; }
  .email       { top: 392px; }
  .postal      { top: 457px; }
</style>
</head>
<body>
  <main class="card">
    <section class="brand-panel">
      <div class="brand-mark" aria-hidden="true"></div>
      <p class="brand-name">The Lumen<br>Collective</p>
    </section>
    <section class="details-panel">
      <p class="detail person-name">Dr. Mara Ellison</p>
      <p class="detail person-role">Director</p>
      <p class="detail company">The Lumen Collective</p>
      <p class="detail mobile">M::: +61400 318 274</p>
      <p class="detail phone">P:::&nbsp; +612 9460 5127</p>
      <p class="detail email">E::: mara@lumencollective.com.au</p>
      <p class="detail postal">PO::: P.O. Box 4417, Elmvale Park, Sydney, Australia</p>
    </section>
  </main>
</body>
</html>
```